Canadian furniture distributor

I need a logo design for my new company, Pellham Craft G.P., Ergonomic High-End furniture distribution (very attractive patented design -mainly Desks & Chairs-).

Can be used for children adults, elders or limited mobility people.

Colors and design should match logo colors and products.

Industry/Entity Type

It Company

```html
<!DOCTYPE html>
<html lang="en">
<head>
<meta charset="utf-8">
<title>Pellham Craft – Business Card</title>
<link rel="stylesheet" href="https://fonts.googleapis.com/css2?family=Righteous&family=Questrial&display=swap">
<style>
  :root {
    --plum: #8e1f4f;
    --amber: #f3b21c;
    --ink: #1e1e1e;
    --card: #ffffff;
    --card-back: #f9fbfd;
    --backdrop: #e6e7e9;
  }
  html, body {
    margin: 0;
    width: 1200px;
    height: 1200px;
    overflow: hidden;
    background: var(--backdrop);
  }
  .canvas {
    position: relative;
    width: 1200px;
    height: 1200px;
  }
  .card {
    position: absolute;
    left: 130px;
    width: 934px;
    height: 530px;
    border-radius: 22px;
    background: var(--card);
    box-shadow: 0 4px 14px rgba(0,0,0,0.18);
    overflow: hidden;
  }
  .card--front { top: 55px; }
  .card--back { top: 612px; background: var(--card-back); }

  .brand-name {
    font-family: "Righteous", sans-serif;
    color: var(--plum);
    white-space: nowrap;
    margin: 0;
    font-weight: 400;
  }

  /* front */
  .front-mark {
    position: absolute;
    left: 48px;
    top: 50px;
    width: 420px;
    height: 434px;
    display: flex;
    flex-direction: column;
    align-items: center;
    justify-content: center;
    gap: 28px;
  }
  .front-mark .mark-square {
    width: 110px;
    height: 110px;
    background: var(--amber);
  }
  .front-mark .brand-name { font-size: 54px; }

  .details {
    position: absolute;
    right: 54px;
    top: 72px;
    text-align: right;
    font-family: "Questrial", sans-serif;
    color: var(--ink);
  }
  .details .brand-name { font-size: 52px; line-height: 1; margin-bottom: 34px; margin-right: -4px; }
  .employee-name { font-size: 22px; color: var(--plum); letter-spacing: 0.5px; line-height: 1.2; }
  .employee-title { font-size: 21px; line-height: 1.3; }
  .address { font-size: 21px; line-height: 1.3; margin-top: 38px; letter-spacing: 0.5px; }
  .contact-list { list-style: none; padding: 0; margin: 26px 0 0; font-size: 25px; line-height: 31px; }
  .contact-list li { display: flex; justify-content: flex-end; align-items: center; gap: 10px; }
  .contact-list svg { width: 20px; height: 20px; flex: none; }

  /* back */
  .back-mark {
    position: absolute;
    left: 88px;
    top: 170px;
    width: 350px;
    display: flex;
    flex-direction: column;
    align-items: center;
    gap: 26px;
  }
  .back-mark .mark-square { width: 90px; height: 90px; background: var(--amber); }
  .back-mark .brand-name { font-size: 50px; }

  .product-photo {
    position: absolute;
    left: 470px;
    top: 44px;
    width: 430px;
    height: 460px;
    border-radius: 10px;
    background: radial-gradient(ellipse at 55% 40%, #e8edf2 0%, #d6dde4 55%, #f3f6f9 100%);
  }
</style>
</head>
<body>
<main class="canvas">

  <section class="card card--front" aria-label="Business card front">
    <div class="front-mark">
      <span class="mark-square"></span>
      <p class="brand-name">Pellham Craft</p>
    </div>
    <div class="details">
      <h1 class="brand-name">Pellham Craft</h1>
      <div class="employee-name">EMPLOYEE NAME</div>
      <div class="employee-title">Title</div>
      <div class="address">2240 Alder Ridge Rd Suite 310,<br>Kelowna BC V1Y 4K8</div>
      <ul class="contact-list">
        <li>250.418.2270
          <svg viewBox="0 0 20 20" aria-hidden="true"><rect x="1" y="1" width="18" height="18" rx="4" fill="var(--amber)"/><path d="M7 5c-1 0-1.5 1-1.2 2.5.6 3 2.8 5.8 5.7 7 1.2.4 2.2 0 2.5-.8l-1.8-1.8-1.4.8c-1.3-.8-2.2-2-2.8-3.3l1-1.2L7 5z" fill="#fff"/></svg></li>
        <li>250.418.2271
          <svg viewBox="0 0 20 20" aria-hidden="true"><rect x="5" y="2" width="10" height="5" fill="var(--amber)"/><rect x="1" y="7" width="18" height="8" rx="2" fill="var(--amber)"/><rect x="5" y="12" width="10" height="6" fill="var(--amber)" stroke="#fff" stroke-width="1.5"/></svg></li>
        <li>hello@pellhamcraft.ca
          <svg viewBox="0 0 20 20" aria-hidden="true"><rect x="1" y="4" width="18" height="12" fill="var(--amber)"/><path d="M1 4l9 7 9-7" fill="none" stroke="#fff" stroke-width="1.5"/></svg></li>
        <li>www.pellhamcraft.ca
          <svg viewBox="0 0 20 20" aria-hidden="true"><g fill="none" stroke="var(--amber)" stroke-width="1.5"><circle cx="10" cy="10" r="8"/><ellipse cx="10" cy="10" rx="3.5" ry="8"/><path d="M2 10h16M3.5 6h13M3.5 14h13"/></g></svg></li>
      </ul>
    </div>
  </section>

  <section class="card card--back" aria-label="Business card back">
    <div class="back-mark">
      <span class="mark-square"></span>
      <p class="brand-name">Pellham Craft</p>
    </div>
    <div class="product-photo" role="img" aria-label="Photo of a white height-adjustable ergonomic desk shown at three tabletop heights"></div>
  </section>

</main>
</body>
</html>
```